Harlow Mailbox Services, full-service collaboration with postal service - installation of units

1. CBU - Cluster Box Unit - These are Mailbox units that you would see at residential neighborhoods, and Apartments -
2. Logo Needed
3. Maybe have CBU as a division of DWFS (Dermot Vance Field Services)
4. Card to be primary Harlow Mailbox Services

This is a letter of introduction that I am developing:

I am writing to introduce Dermot Vance Field Services, a company dedicated to delivering exceptional service and quality in the installation and maintenance of commercial mailboxes, specifically Cluster Box Units (CBUs). Our commitment to excellence and customer satisfaction has established us as a trusted partner for developers and postal services alike.
At Dermot Vance Field Services, we take pride in our comprehensive approach, ensuring that every step of the mailbox installation process is handled with precision and care. Our services include:
• Supplying high-quality CBUs tailored to meet the specific needs of your development.
• Providing a CBU plat layout upon approval of the address plat, ensuring seamless integration into your development plans.
• Collaborating with developers and postmasters to determine the optimal CBU locations for efficient mail delivery.
• Qualifying the labeling of CBU units, offering both sticker and etching options to suit your preferences.
• Pouring durable concrete foundations as required for the secure installation of the CBU units.
• Handling the installation process with expertise and attention to detail.
• Labeling the units and supplying keys for each mailbox, ensuring a smooth transition for residents and businesses.
Our team is dedicated to working closely with you to ensure that all requirements are met and that the installation process is completed efficiently and to the highest standards.
We look forward to the opportunity to collaborate with you and contribute to the success of your project. Please do not hesitate to contact us for any additional information or to discuss your specific requirements.
Sincerely,
Dermot Vance
Dermot Vance Field Services

Target Market(s)

Developers, Builders, Apartment's, HOA

Industry/Entity Type

Construction

Contact Information for Business Card

Name: Dermot Vance, Cell:555-671-0148, Email: derm@dvfieldco.example

Font styles to use
Serif

Requirements
Must have
• Fresh Looking
Nice to have
• Maybe a CBU Box if it looks clean
Should not have
• Not Industrial or Old traditional card

```html
<!DOCTYPE html>
<html lang="en">
<head>
<meta charset="utf-8">
<title>Harlow Mailbox Services — Business Card</title>
<link href="https://fonts.googleapis.com/css2?family=Exo+2:wght@400;600;700&display=swap" rel="stylesheet">
<style>
  :root {
    --brand-blue: #14a2c4;
    --brand-green: #3aaa49;
    --text-grey: #8a8a8a;
    --paper: #ffffff;
    --canvas: #ffffff;
  }
  * { box-sizing: border-box; margin: 0; padding: 0; }
  html, body { width: 960px; height: 1200px; overflow: hidden; background: var(--canvas); }
  body { position: relative; font-family: "Exo 2", sans-serif; }

  .card {
    position: absolute;
    left: 60px;
    width: 840px;
    height: 480px;
    overflow: hidden;
    box-shadow: 14px 16px 24px rgba(0,0,0,0.28);
  }
  .card--front { top: 86px; background: var(--paper); }
  .card--back { top: 634px; background: var(--brand-blue); }

  .accent-bar {
    position: absolute;
    left: 165px;
    width: 37px;
    background: var(--brand-blue);
  }
  .accent-bar--top { top: 0; height: 126px; }
  .accent-bar--bottom { top: 353px; height: 127px; }

  .wordmark {
    position: absolute;
    display: flex;
    flex-direction: column;
    align-items: center;
    text-transform: uppercase;
    font-weight: 700;
    text-align: center;
  }
  .wordmark__square { display: block; }
  .wordmark__name { line-height: 1; }

  .card--front .wordmark {
    left: 62px; top: 180px; width: 240px;
    color: var(--brand-green);
  }
  .card--front .wordmark__square {
    width: 46px; height: 46px; background: var(--brand-blue); margin-bottom: 14px;
  }
  .card--front .wordmark__name { font-size: 22px; letter-spacing: 6px; }
  .card--front .wordmark__sub { font-size: 15px; letter-spacing: 3px; margin-top: 6px; }

  .card--back .wordmark {
    left: 0; top: 150px; width: 840px;
    color: var(--paper);
  }
  .card--back .wordmark__square {
    width: 84px; height: 84px; background: var(--paper); margin-bottom: 26px;
  }
  .card--back .wordmark__name { font-size: 40px; letter-spacing: 14px; }
  .card--back .wordmark__sub { font-size: 26px; letter-spacing: 5px; margin-top: 12px; }

  .contact {
    position: absolute;
    left: 462px; top: 160px; right: 0;
  }
  .contact__name {
    font-size: 31px;
    font-weight: 700;
    text-transform: uppercase;
    letter-spacing: 0.5px;
    color: var(--brand-blue);
    line-height: 1;
    padding: 0 0 16px 0;
  }
  .contact__name .surname { color: var(--brand-green); }
  .contact__rule { height: 2px; background: var(--brand-blue); }
  .contact__list { list-style: none; padding: 10px 0 10px; }
  .contact__item {
    display: flex; align-items: center; gap: 10px;
    font-size: 24px; font-weight: 400; color: var(--text-grey);
    height: 38px;
  }
  .contact__icon { width: 28px; height: 28px; flex: none; }
</style>
</head>
<body>

  <section class="card card--front" aria-label="Business card front">
    <div class="accent-bar accent-bar--top"></div>
    <div class="accent-bar accent-bar--bottom"></div>

    <div class="wordmark">
      <span class="wordmark__square"></span>
      <span class="wordmark__name">Harlow</span>
      <span class="wordmark__sub">Mailbox Services</span>
    </div>

    <div class="contact">
      <h1 class="contact__name">Dermot <span class="surname">Vance</span></h1>
      <div class="contact__rule"></div>
      <ul class="contact__list">
        <li class="contact__item">
          <svg class="contact__icon" viewBox="0 0 28 28" aria-hidden="true">
            <circle cx="14" cy="14" r="14" fill="#14a2c4"/>
            <path d="M9.5 7.5c.8-.5 1.7-.3 2.2.5l1.3 2.2c.4.7.2 1.5-.4 2l-1 .8c.7 1.6 2 2.9 3.5 3.6l.8-1c.5-.6 1.3-.8 2-.4l2.2 1.3c.8.5 1 1.4.5 2.2l-.7 1c-.8 1.1-2.3 1.5-3.6.9-3.4-1.5-6.1-4.2-7.6-7.6-.6-1.3-.2-2.8.9-3.6z" fill="#fff"/>
          </svg>
          <span>555-671-0148</span>
        </li>
        <li class="contact__item">
          <svg class="contact__icon" viewBox="0 0 28 28" aria-hidden="true">
            <circle cx="14" cy="14" r="14" fill="#14a2c4"/>
            <rect x="7" y="9" width="14" height="10" rx="1" fill="none" stroke="#fff" stroke-width="1.6"/>
            <path d="M7.5 9.8 14 14.8l6.5-5M7.5 18.4l4.6-4.3M20.5 18.4l-4.6-4.3" fill="none" stroke="#fff" stroke-width="1.4"/>
          </svg>
          <span>derm@dvfieldco.example</span>
        </li>
      </ul>
      <div class="contact__rule"></div>
    </div>
  </section>

  <section class="card card--back" aria-label="Business card back">
    <div class="wordmark">
      <span class="wordmark__square"></span>
      <span class="wordmark__name">Harlow</span>
      <span class="wordmark__sub">Mailbox Services</span>
    </div>
  </section>

</body>
</html>
```